Tarvimoor business cards

Need fresh design for our business cards. Logo must be specific, we are open for everything else.

Contact Information for Business Card

phrase "GMP & JANITORIAL SERVICES" should be used as main point of card

Colors
3176b5
3276b5
85acd3
cedeed
ffffff
0292cd
33a6d7
85cae6
cee9f5

Requirements
Must have
• The logo
Should not have
• crowded designs

```html
<!DOCTYPE html>
<html lang="en">
<head>
<meta charset="utf-8">
<title>Tarvimoor business cards</title>
<link href="https://fonts.googleapis.com/css2?family=Josefin+Sans:wght@400&family=Questrial&display=swap" rel="stylesheet">
<style>
  :root {
    --stage: #0a6aa6;
    --card: #ffffff;
    --brand-blue: #1a7bbf;
    --soft-blue: #85acd3;
    --mist: #eef3f8;
    --mist-edge: #f9fbfd;
  }
  * { margin: 0; padding: 0; box-sizing: border-box; }
  html, body {
    width: 1200px;
    height: 1200px;
    overflow: hidden;
    background: var(--stage);
  }
  .stage {
    position: relative;
    width: 1200px;
    height: 1200px;
  }
  .card {
    position: absolute;
    left: 267px;
    width: 666px;
    height: 370px;
    background: var(--card);
  }
  .card--front { top: 203px; }
  .card--back { top: 625px; }

  .droplet-texture {
    position: absolute;
    inset: 0;
    background: radial-gradient(ellipse at center, var(--card) 30%, var(--mist-edge) 60%, var(--mist) 100%);
  }
  .front-wordmark {
    position: absolute;
    left: 0;
    right: 0;
    top: 150px;
    text-align: center;
    font-family: "Josefin Sans", sans-serif;
    font-weight: 400;
    font-size: 64px;
    line-height: 1;
    letter-spacing: 0.12em;
    color: var(--brand-blue);
  }

  .tagline {
    position: absolute;
    left: 0;
    right: 0;
    top: 56px;
    text-align: center;
    font-family: "Questrial", sans-serif;
    font-size: 42px;
    line-height: 1;
    color: var(--soft-blue);
  }
  .person {
    position: absolute;
    right: 378px;
    top: 176px;
    text-align: right;
    font-family: "Questrial", sans-serif;
    color: var(--brand-blue);
  }
  .person__brand {
    font-family: "Josefin Sans", sans-serif;
    font-size: 25px;
    letter-spacing: 0.12em;
    margin-right: -0.12em;
    line-height: 1;
    margin-bottom: 38px;
  }
  .person__name {
    font-size: 45px;
    line-height: 45px;
    letter-spacing: -0.01em;
  }
  .contacts {
    position: absolute;
    left: 348px;
    top: 225px;
    list-style: none;
    font-family: "Questrial", sans-serif;
    font-size: 17px;
    color: var(--soft-blue);
  }
  .contacts__item {
    display: flex;
    align-items: center;
    height: 27.6px;
  }
  .contacts__item--address { font-size: 15.5px; }
  .contacts__icon {
    width: 14px;
    height: 14px;
    margin-right: 12px;
    flex: none;
  }
</style>
</head>
<body>
<main class="stage">
  <section class="card card--front">
    <div class="droplet-texture" role="img" aria-label="Scattered water droplets pattern"></div>
    <div class="front-wordmark">TARVIMOOR</div>
  </section>

  <section class="card card--back">
    <h1 class="tagline">GMP &amp; JANITORIAL SERVICES</h1>

    <div class="person">
      <div class="person__brand">TARVIMOOR</div>
      <div class="person__name">NAME</div>
      <div class="person__name">LAST NAME</div>
    </div>

    <ul class="contacts">
      <li class="contacts__item contacts__item--address">
        <svg class="contacts__icon" viewBox="0 0 14 14" aria-hidden="true">
          <path d="M7 1a4.2 4.2 0 0 0-4.2 4.2C2.8 8.4 7 13 7 13s4.2-4.6 4.2-7.8A4.2 4.2 0 0 0 7 1z" fill="#85acd3"/>
          <circle cx="7" cy="5.2" r="1.6" fill="#fff"/>
        </svg>
        No#, Main Road,Main Road 2, City
      </li>
      <li class="contacts__item">
        <svg class="contacts__icon" viewBox="0 0 14 14" aria-hidden="true">
          <g fill="none" stroke="#85acd3" stroke-width="1.3">
            <circle cx="7" cy="7" r="5.5"/>
            <ellipse cx="7" cy="7" rx="2.4" ry="5.5"/>
            <line x1="1.5" y1="7" x2="12.5" y2="7"/>
          </g>
        </svg>
        0888 888 888
      </li>
      <li class="contacts__item">
        <svg class="contacts__icon" viewBox="0 0 14 14" aria-hidden="true">
          <rect x="3.5" y="1" width="7" height="12" rx="1.2" fill="none" stroke="#85acd3" stroke-width="1.3"/>
          <line x1="6" y1="11" x2="8" y2="11" stroke="#85acd3" stroke-width="1.1"/>
        </svg>
        hello@tarvimoor.com
      </li>
      <li class="contacts__item">
        <svg class="contacts__icon" viewBox="0 0 14 14" aria-hidden="true">
          <rect x="1" y="3" width="12" height="8" fill="#85acd3"/>
          <path d="M1 3l6 4.5L13 3" fill="none" stroke="#fff" stroke-width="1"/>
        </svg>
        tarvimoor.com
      </li>
    </ul>
  </section>
</main>
</body>
</html>
```